Animal Hospital Business Cards

Make a business card look like the attached example

*Use the same blue/black coloring
*Fenbrook Hollow Animal Hospital (instead of mobile pet rounds)
*Emergency Services (instead of tri-county care center)
*House Calls (instead of open 7 days by appointment)
*Change address to 1873 Tilden Marsh Rd Brindle Falls, OH 45199
*Open 7 days a week (instead of emergency service)
*Add the website www.fenbrookhollowanimalhospital.example

On the back...
*instead of the text outlined in red, just white
*instead of the light blue, try your best to make it just like the blue and black on the front side of the card
*Delete "designed and printed by Blue Heron Print Co, www.blueheronprintco.example

Requirements
Must have
• look just like the attached example with requested edits/changes

```html
<!DOCTYPE html>
<html lang="en">
<head>
<meta charset="utf-8">
<title>Fenbrook Hollow Animal Hospital – Business Card</title>
<link rel="stylesheet" href="https://fonts.googleapis.com/css2?family=Tinos:wght@700&family=Oswald:wght@500;600&family=Roboto+Condensed:wght@700&family=Roboto:wght@400;500&display=swap">
<style>
  :root {
    --page: #e8e8e8;
    --card: #f4f4f3;
    --teal-dark: #164a59;
    --teal-light: #4e7f8d;
    --black: #0b0b0b;
    --stripe-grey: #b9bcbd;
    --ink: #111111;
    --accent-red: #9b2230;
    --slate: #606a86;
    --label: #5a6684;
    --rule: #7c879f;
    --white: #ffffff;
    --mon: #b0506e; --tue: #d8692f; --wed: #4f86a3; --thu: #a81e2a;
    --fri: #c0a22b; --sat: #9a3a4e; --sun: #1f5a2f;
  }
  * { box-sizing: border-box; margin: 0; padding: 0; }
  html, body { width: 1125px; height: 1200px; overflow: hidden; background: var(--page); }

  .card {
    position: absolute; left: 150px; width: 824px; height: 471px;
    border-radius: 22px; overflow: hidden; background: var(--card);
  }
  .card--front { top: 98px; }
  .card--back { top: 632px; }

  .bands { position: absolute; inset: 0; width: 100%; height: 100%; }
  .abs { position: absolute; }
  .centered { left: 0; right: 0; text-align: center; transform: translateY(-50%); }

  .serif { font-family: "Tinos", "Times New Roman", serif; font-weight: 700; }
  .front-title { top: 40px; color: var(--white); font-size: 50px; letter-spacing: 0.5px; white-space: nowrap; }
  .front-doctor { top: 128px; color: var(--ink); font-size: 37px; }
  .logo-name { top: 200px; color: var(--ink); font-size: 20px; }
  .species { top: 263px; color: var(--ink); font-size: 25px; }
  .species .dot { color: var(--accent-red); }
  .website { top: 294px; font-family: "Roboto Condensed", "Arial Narrow", sans-serif; font-weight: 700; font-size: 23px; color: var(--ink); white-space: nowrap; }
  .front-phone { top: 341px; color: var(--accent-red); font-size: 46px; }
  .front-tagline { top: 433px; color: var(--white); font-size: 50px; }

  .side { position: absolute; top: 205px; width: 145px; font-family: "Oswald", "Arial Narrow", sans-serif; color: var(--ink); }
  .side--left { left: 36px; text-align: left; }
  .side--right { right: 36px; text-align: right; }
  .side__heading { font-size: 32px; line-height: 34px; font-weight: 600; text-transform: uppercase; letter-spacing: -0.5px; }
  .side__rule { height: 2px; background: var(--accent-red); margin: 14px 0 20px; }
  .side__note { font-size: 15px; line-height: 21px; font-weight: 600; text-transform: uppercase; letter-spacing: -0.3px; white-space: nowrap; }

  .back-header { position: absolute; top: 0; left: 0; right: 0; height: 191px; background: var(--slate); }
  .back-title { top: 46px; color: var(--white); font-size: 48px; letter-spacing: 0.5px; }
  .back-doctor { top: 97px; color: var(--white); font-size: 36px; }
  .back-phone { top: 146px; color: var(--white); font-size: 46px; }

  .form-row { position: absolute; left: 51px; right: 51px; display: flex; align-items: flex-end;
    font-family: "Roboto", Arial, sans-serif; font-size: 25px; color: var(--label); }
  .form-row--name { top: 228px; }
  .form-row--when { top: 398px; }
  .blank { border-bottom: 2px solid var(--rule); margin: 0 2px 6px; height: 2px; }
  .form-row--name .blank { flex: 1; }
  .blank--date { width: 254px; }
  .blank--time { width: 238px; }
  .ampm { font-size: 21px; margin-left: 2px; margin-bottom: 2px; }

  .days { position: absolute; top: 296px; left: 0; right: 0; height: 64px; }
  .bone {
    position: absolute; width: 84px; height: 64px; color: var(--white);
    font-family: "Roboto", Arial, sans-serif; font-weight: 500; font-size: 22px;
    display: flex; align-items: center; justify-content: center; z-index: 0;
  }
  .bone::before {
    content: ""; position: absolute; z-index: -1; inset: 0;
    background:
      radial-gradient(circle at 15px 16px, currentColor 15px, transparent 15.5px),
      radial-gradient(circle at 15px 48px, currentColor 15px, transparent 15.5px),
      radial-gradient(circle at 69px 16px, currentColor 15px, transparent 15.5px),
      radial-gradient(circle at 69px 48px, currentColor 15px, transparent 15.5px),
      linear-gradient(currentColor, currentColor) 12px 14px / 60px 36px no-repeat;
    color: var(--bone);
  }
  .bone span { color: var(--white); }
  .bone--mon { left: 49px;  --bone: var(--mon); }
  .bone--tue { left: 157px; --bone: var(--tue); }
  .bone--wed { left: 266px; --bone: var(--wed); }
  .bone--thu { left: 372px; --bone: var(--thu); }
  .bone--fri { left: 480px; --bone: var(--fri); }
  .bone--sat { left: 586px; --bone: var(--sat); }
  .bone--sun { left: 692px; --bone: var(--sun); }
</style>
</head>
<body>

<section class="card card--front" aria-label="Business card front">
  <svg class="bands" viewBox="0 0 800 457" preserveAspectRatio="none" aria-hidden="true">
    <defs>
      <linearGradient id="tealSweep" x1="0" x2="1" y1="0" y2="0">
        <stop offset="0" stop-color="var(--teal-dark)"/>
        <stop offset="0.5" stop-color="var(--teal-light)"/>
        <stop offset="1" stop-color="var(--teal-dark)"/>
      </linearGradient>
    </defs>
    <polygon points="0,0 800,0 800,96 0,58" fill="url(#tealSweep)"/>
    <polygon points="0,56 600,86 0,92" fill="var(--black)"/>
    <polygon points="0,92 800,94 800,97 0,96" fill="var(--stripe-grey)"/>
    <polygon points="0,366 800,360 800,372 0,370" fill="var(--stripe-grey)"/>
    <polygon points="0,370 800,371 800,408 200,380" fill="var(--black)"/>
    <polygon points="0,370 200,380 800,408 800,457 0,457" fill="url(#tealSweep)"/>
  </svg>

  <h1 class="abs centered serif front-title">Fenbrook Hollow Animal Hospital</h1>
  <p class="abs centered serif front-doctor">Marcus L. Pendry, DVM</p>
  <p class="abs centered serif logo-name">Fenbrook Hollow</p>
  <p class="abs centered serif species">Cats <span class="dot">•</span> Dogs <span class="dot">•</span> Birds <span class="dot">•</span> Exotics</p>
  <p class="abs centered website">www.fenbrookhollowanimalhospital.example</p>
  <p class="abs centered serif front-phone">(513) 555-0147</p>

  <div class="side side--left">
    <p class="side__heading">Emergency<br>Services</p>
    <div class="side__rule"></div>
    <p class="side__note">1873 Tilden Marsh Rd<br>Brindle Falls, OH 45199</p>
  </div>
  <div class="side side--right">
    <p class="side__heading">House<br>Calls</p>
    <div class="side__rule"></div>
    <p class="side__note">30 Years<br>of Experience</p>
  </div>

  <p class="abs centered serif front-tagline">Open 7 days a week</p>
</section>

<section class="card card--back" aria-label="Appointment card back">
  <header class="back-header">
    <h2 class="abs centered serif back-title">Veterinary Appointment</h2>
    <p class="abs centered serif back-doctor">Marcus L. Pendry, DVM</p>
    <p class="abs centered serif back-phone">(513) 555-0147</p>
  </header>

  <div class="form-row form-row--name">
    <span>Your appointment for</span><span class="blank"></span><span>is on</span>
  </div>

  <div class="days">
    <div class="bone bone--mon"><span>Mon</span></div>
    <div class="bone bone--tue"><span>Tues</span></div>
    <div class="bone bone--wed"><span>Wed</span></div>
    <div class="bone bone--thu"><span>Thur</span></div>
    <div class="bone bone--fri"><span>Fri</span></div>
    <div class="bone bone--sat"><span>Sat</span></div>
    <div class="bone bone--sun"><span>Sun</span></div>
  </div>

  <div class="form-row form-row--when">
    <span>Date</span><span class="blank blank--date"></span>
    <span>Time</span><span class="blank blank--time"></span>
    <span class="ampm">AM/PM</span>
  </div>
</section>

</body>
</html>
```